professional business card design

Business card design. Photos have been uploaded and i am open to the designer choosing which photos to use. Would like the card to be mostyly in a grey scale design with black, whites, silver & grey colours. I have added copy of our flyer as would like on the back side of card our services to be listed. Do not use any bright colurs such as blue red green or yellow. i need to be able to edit the phone number and naem in the final card design submitted.

Target Market(s)

Clients

Industry/Entity Type

earhmovibng and transport

Contact Information for Business Card

Director Name, address, email, phone number and services

Colors

Designer to choose only greyscale colors for use in the design.

Requirements
Should not have
• no yellow, red, blue or green

```html
<!DOCTYPE html>
<html lang="en">
<head>
<meta charset="UTF-8">
<title>KTS Pty Ltd – Business Card</title>
<link rel="stylesheet" href="https://fonts.googleapis.com/css2?family=Oswald:wght@300;400;600&display=swap">
<style>
  :root {
    --ink: #1e1e1e;
    --black: #231f20;
    --panel-grey: #bcbdc0;
    --steel-dark: #1a1a1a;
    --steel-mid: #3a3a3c;
    --silver: #c9c9cb;
    --white: #ffffff;
    --row-dark: #a6a7a9;
    --row-light: #e4e4e5;
    --tan: #c9a96a;
  }
  * { margin: 0; padding: 0; box-sizing: border-box; }
  html, body { width: 1027px; height: 1200px; overflow: hidden; background: var(--white); }
  body { font-family: "Oswald", sans-serif; color: var(--ink); }
  .card { position: relative; width: 1027px; height: 1200px; background: var(--white); overflow: hidden; }

  .masthead {
    position: absolute; left: 0; top: 0; width: 1027px; height: 361px;
    background: radial-gradient(ellipse at 50% 40%, var(--steel-mid) 0%, var(--steel-dark) 75%);
  }
  .brand {
    position: absolute; left: 0; top: 20px; width: 1027px; text-align: center;
    font-weight: 600; color: var(--silver); line-height: 1;
  }
  .brand-name { display: block; font-size: 230px; letter-spacing: 6px; }
  .brand-suffix { display: block; font-size: 56px; margin-top: 14px; }

  .identity {
    position: absolute; left: 0; top: 361px; width: 514px; height: 224px;
    background: var(--black); color: var(--white); text-align: center; font-weight: 300;
  }
  .identity .name { position: absolute; top: 52px; width: 100%; font-size: 48px; line-height: 1; }
  .identity .title { position: absolute; top: 128px; width: 100%; font-size: 30px; line-height: 1; }

  .contact {
    position: absolute; left: 514px; top: 361px; width: 513px; height: 224px;
    background: var(--panel-grey); list-style: none; padding: 26px 0 0 34px;
  }
  .contact li { display: flex; align-items: center; height: 44px; font-size: 27px; font-weight: 300; color: var(--ink); }
  .contact svg { width: 30px; height: 30px; margin-right: 12px; flex: none; }

  .services-heading {
    position: absolute; left: 50px; top: 652px; font-size: 52px; font-weight: 300; line-height: 1;
  }
  .service-list { position: absolute; list-style: none; top: 733px; }
  .service-list.left { left: 50px; width: 440px; }
  .service-list.right { left: 533px; width: 442px; }
  .service-list li {
    display: flex; align-items: flex-start; min-height: 37.5px; padding-top: 3px;
    font-size: 27px; font-weight: 300; line-height: 1.2;
    background: linear-gradient(90deg, var(--row-dark) 0%, var(--row-light) 55%, rgba(255,255,255,0) 100%);
  }
  .service-list li:nth-child(even) {
    background: linear-gradient(90deg, var(--row-light) 0%, #f2f2f2 55%, rgba(255,255,255,0) 100%);
  }
  .service-list li.two-line { min-height: 75px; }
  .tick { width: 20px; height: 20px; margin: 7px 28px 0 28px; flex: none; }

  .more-note {
    position: absolute; left: 50px; top: 1044px; font-size: 26px; font-weight: 300; line-height: 1;
  }
  .cta-band {
    position: absolute; left: 0; top: 1087px; width: 1027px; height: 113px; background: var(--black);
  }
  .cta {
    position: absolute; left: 50px; top: 1103px; color: var(--tan);
    font-size: 33px; font-weight: 600; line-height: 42px;
  }
  .truck-photo {
    position: absolute; left: 555px; top: 1000px; width: 472px; height: 200px;
    background: linear-gradient(100deg, rgba(220,220,220,0.9) 0%, #8a8a8c 45%, #2b2e36 75%, #1c1c1e 100%);
    clip-path: polygon(0 55%, 45% 40%, 55% 5%, 100% 20%, 100% 100%, 0 100%);
  }
</style>
</head>
<body>
<main class="card">
  <header class="masthead">
    <div class="brand">
      <span class="brand-name">KTS</span>
      <span class="brand-suffix">Pty Ltd</span>
    </div>
  </header>

  <section class="identity">
    <p class="name">DIRECTOR NAME</p>
    <p class="title">DIRECTOR NAME</p>
  </section>

  <ul class="contact">
    <li>
      <svg viewBox="0 0 30 30"><circle cx="15" cy="15" r="12.5" fill="none" stroke="#1e1e1e" stroke-width="2.2"/><path d="M10 9.5c1-1 2-.8 2.6.2l1 1.8c.4.8.1 1.4-.6 2l-.5.4c.8 1.7 1.8 2.8 3.5 3.6l.5-.5c.6-.7 1.3-.9 2-.5l1.8 1c1 .6 1.1 1.6.2 2.6-1.4 1.5-3.6 1.2-6-.7-2.4-1.9-4.3-4.4-4.8-6.5-.3-1.4 0-2.6.3-3.4z" fill="#1e1e1e"/></svg>
      000-00000
    </li>
    <li>
      <svg viewBox="0 0 30 30"><rect x="2" y="7" width="26" height="17" fill="none" stroke="#1e1e1e" stroke-width="2"/><path d="M2 7l13 10 13-10M2 24l9.5-9M28 24l-9.5-9" fill="none" stroke="#1e1e1e" stroke-width="2"/></svg>
      COMPANYNAME.EMAIL.COM
    </li>
    <li>
      <svg viewBox="0 0 30 30"><path d="M15 28C9 19 6 15 6 11a9 9 0 0 1 18 0c0 4-3 8-9 17z" fill="none" stroke="#1e1e1e" stroke-width="2"/><circle cx="15" cy="11" r="3.5" fill="none" stroke="#1e1e1e" stroke-width="2"/></svg>
      COMPANY, ADDRESS
    </li>
    <li>
      <svg viewBox="0 0 30 30"><circle cx="15" cy="15" r="12" fill="#1e1e1e"/><path d="M3 15h24M15 3v24M6 8.5h18M6 21.5h18" stroke="#bcbdc0" stroke-width="1.4"/><ellipse cx="15" cy="15" rx="6" ry="12" fill="none" stroke="#bcbdc0" stroke-width="1.4"/></svg>
      WEBSITE.COM
    </li>
  </ul>

  <h2 class="services-heading">SERVICES</h2>

  <ul class="service-list left">
    <li><svg class="tick" viewBox="0 0 20 20"><rect x="1" y="3" width="15" height="15" fill="none" stroke="#c9a96a" stroke-width="2"/><path d="M5 10l4 4 9-11" fill="none" stroke="#c9a96a" stroke-width="2.2"/></svg>OVER SIZE LOADS / HOT SHOT LOADS</li>
    <li><svg class="tick" viewBox="0 0 20 20"><rect x="1" y="3" width="15" height="15" fill="none" stroke="#c9a96a" stroke-width="2"/><path d="M5 10l4 4 9-11" fill="none" stroke="#c9a96a" stroke-width="2.2"/></svg>HEAVY VEHICLE RECOVERY SERVICES</li>
    <li><svg class="tick" viewBox="0 0 20 20"><rect x="1" y="3" width="15" height="15" fill="none" stroke="#c9a96a" stroke-width="2"/><path d="M5 10l4 4 9-11" fill="none" stroke="#c9a96a" stroke-width="2.2"/></svg>POTABLE WATER DELIVERIES</li>
    <li><svg class="tick" viewBox="0 0 20 20"><rect x="1" y="3" width="15" height="15" fill="none" stroke="#c9a96a" stroke-width="2"/><path d="M5 10l4 4 9-11" fill="none" stroke="#c9a96a" stroke-width="2.2"/></svg>ROAD BUILDING / MAINTENTANCE</li>
    <li><svg class="tick" viewBox="0 0 20 20"><rect x="1" y="3" width="15" height="15" fill="none" stroke="#c9a96a" stroke-width="2"/><path d="M5 10l4 4 9-11" fill="none" stroke="#c9a96a" stroke-width="2.2"/></svg>EARTHWORKS</li>
    <li><svg class="tick" viewBox="0 0 20 20"><rect x="1" y="3" width="15" height="15" fill="none" stroke="#c9a96a" stroke-width="2"/><path d="M5 10l4 4 9-11" fill="none" stroke="#c9a96a" stroke-width="2.2"/></svg>SAND &amp; METAL SUPPLY &amp; CARTAGE</li>
  </ul>

  <ul class="service-list right">
    <li><svg class="tick" viewBox="0 0 20 20"><rect x="1" y="3" width="15" height="15" fill="none" stroke="#c9a96a" stroke-width="2"/><path d="M5 10l4 4 9-11" fill="none" stroke="#c9a96a" stroke-width="2.2"/></svg>ROAD TRAIN TIPPERS</li>
    <li><svg class="tick" viewBox="0 0 20 20"><rect x="1" y="3" width="15" height="15" fill="none" stroke="#c9a96a" stroke-width="2"/><path d="M5 10l4 4 9-11" fill="none" stroke="#c9a96a" stroke-width="2.2"/></svg>ROAD TRAIN TANKERS</li>
    <li><svg class="tick" viewBox="0 0 20 20"><rect x="1" y="3" width="15" height="15" fill="none" stroke="#c9a96a" stroke-width="2"/><path d="M5 10l4 4 9-11" fill="none" stroke="#c9a96a" stroke-width="2.2"/></svg>ROAD TRAIN FLAT TOPS</li>
    <li><svg class="tick" viewBox="0 0 20 20"><rect x="1" y="3" width="15" height="15" fill="none" stroke="#c9a96a" stroke-width="2"/><path d="M5 10l4 4 9-11" fill="none" stroke="#c9a96a" stroke-width="2.2"/></svg>DROP DECK TRAILERS</li>
    <li class="two-line"><svg class="tick" viewBox="0 0 20 20"><rect x="1" y="3" width="15" height="15" fill="none" stroke="#c9a96a" stroke-width="2"/><path d="M5 10l4 4 9-11" fill="none" stroke="#c9a96a" stroke-width="2.2"/></svg><span>MINE SITE ACCREDITED<br>EQUIPMENT &amp; OPERATORS</span></li>
  </ul>

  <p class="more-note">WE OFFER A LARGE RANGE OF SERVICES NOT LISTED SO</p>
  <div class="cta-band"></div>
  <p class="cta">CALL US TODAY FOR A PERSONALISED<br>QUOTE TO SUIT YOUR NEEDS.</p>
  <div class="truck-photo" role="img" aria-label="Photo of a dark road train prime mover hauling silver tanker trailers"></div>
</main>
</body>
</html>
```